A live music performing company website

Hello guys!

We provide live music performance at wedding parties, business exhibitions, and dinner parties. We have three performing teams, a classic music team, a Jazz music team, and a pop music team, in the company.

We already have a logo. Now we are looking for a website proposal which should fin in with the logo and our company style. What we intend to represent is professional, elegant, and luxury atmosphere in the web design.

== Here is the spec ==

* The IA(Information Architecture) of the site will be ("Home" is the root node, "-" is the first sub-layer, "+" is the second sub-layer):

Home
- Groups(brief intro)
+Classic (detail intro)
+Jazz (detail intro)
+Pop (detail intro)
- Members
- Videos
+ Classic
+ Jazz
+ Pop
- Pricing
- Order

*One home page.

*Several internal pages:
- One is used to brief the three performing groups. ("Groups" in the IA)
++ Three pages(or tags) to introduce each groups.
- One is for introducing our primary members ("Members" in the iA)
- One is MV sharing for each performing group. ("Videos" in the IA)
- One is for introducing our pricing packages. ("Pricing" in the IA)
- One is for making order (holds a html form). ("Order" in the IA)
- One is for usual intro pages, such as "contact us", "about us", "Jobs" ...

=== Update 2011/08/29 ===
We also need a theme for our Blog, you can assume it hosts by Quillo.

The theme has to represent the same atmosphere with the main site.
======
Updates

We just add a requirement in the "overview" section. We need a theme for your blog system. We have raised our budget from to 400, and add 2 participation payment.

Thanks!!

Just uploaded a .pdf, which includes our company name and slogan. The logo has been uploaded as an .ai file yesterday.

We have added a requirement in the "Must Have Priorities", which is about the home page.

We have added a "Nice to Have Priorities", which is about a "Chatterpage Like box" element on the home page.

Please check it up. Thanks!!!

About the "Photo slider", we prefer the sixth and seventh one in this page.

http://codetrailnotes.brimwaylab.net/web-programming/47-scripting/85-30-best-photo-plugins-sliders-slideshow-galleries-and-scrollers.html

Target Market(s)

*People who are going to get married in the near future.

*People who are going to launch a dinner party.

*Business people who are going to raise an exhibition.

Industry/Entity Type

Wedding

Requirements
Must have
• *Home page:
+ An area will be used to put a photo slider to show our recent performances.
+ Must be arranged at the resolution of 960px * 600px.
+ Has to present the company name, the logo, and the slogan. How to arrange all of them is up to designer. (Company name and slogan are written in Chinese, they are saved in the pdf as an attachment file.)

*Internal pages:
+ The width of internal pages has to be 960px.

* "Videos" page:
+ Has the capability to arrange the videos by:
- Date (Default arrangement)
- Geo location (With a Wandero map, once our customers click on the pin, the web page could show a list of recording at the location.)
- Category (Biz exhibitions, wedding parties, or dinner parties)
Nice to have
• * Designers can use the preview photos(with watermark) on Pixvaultery.com. We can go to purchase the legal usage once your design has been accepted.

* If it's possible to embed a "Chatterpage Like box" (Please reference it at: http://developers.chatterpage.net/docs/reference/plugins/like-box/) on the home page, it will be great. But if the box might threat the integrity of the page, then don't use it.
Should not have
• * No Flash.
* No tech coding.

```html
<!DOCTYPE html>
<html lang="en">
<head>
<meta charset="utf-8">
<title>悅音藝術 – Wedding music</title>
<link rel="stylesheet" href="https://fonts.googleapis.com/css2?family=Roboto+Condensed:wght@300;400;700&family=Noto+Sans+TC:wght@400&display=swap">
<style>
  :root {
    --backdrop: #e6e6e6;
    --page: #ffffff;
    --band-dark: #2f2f2f;
    --orange: #d9700f;
    --orange-dark: #b85a08;
    --ribbon-light: #f4f4f4;
    --ribbon-shade: #c9c9c9;
    --nav-text: #3a3a3a;
    --heading-grey: #6b6b6b;
    --body-text: #2b2b2b;
    --accent-orange: #d9700f;
    --footer-text: #e8e8e8;
    --logo-mark: #b3261e;
  }
  * { box-sizing: border-box; margin: 0; padding: 0; }
  html, body { width: 1200px; height: 900px; overflow: hidden; background: var(--backdrop); }
  body { position: relative; font-family: "Roboto Condensed", "Arial Narrow", sans-serif; }

  .site { position: absolute; left: 55px; top: 108px; width: 1091px; height: 682px; background: var(--page); overflow: hidden; }

  .top-band { position: absolute; left: 0; top: 0; width: 1091px; height: 49px;
    background: linear-gradient(90deg, #cfcfcf 0%, #6a6a6a 18%, #2f2f2f 35%, #2f2f2f 62%, #7a7a7a 78%, #d8d8d8 100%); }

  .header-fade { position: absolute; left: 0; top: 49px; width: 460px; height: 203px;
    background: linear-gradient(90deg, #ffffff 0%, #ffffff 60%, #e9e9e9 100%); }

  .hero-photo { position: absolute; left: 39px; top: 79px; width: 310px; height: 200px;
    background: radial-gradient(ellipse at 55% 45%, #8a3f12 0%, #b86a2e 28%, #efe6d4 55%, #f6f1e6 80%, rgba(255,255,255,0) 100%); }

  .brand-panel { position: absolute; left: 449px; top: 49px; width: 642px; height: 203px;
    background: linear-gradient(180deg, var(--orange) 0%, var(--orange-dark) 100%); }
  .brand-panel::before { content: ""; position: absolute; left: -14px; top: 72px; width: 28px; height: 48px;
    background: var(--orange); border-radius: 14px 0 0 14px; }

  .brand-dot { position: absolute; left: 92px; top: 36px; width: 62px; height: 62px; border-radius: 50%; background: var(--logo-mark); }
  .brand-name { position: absolute; left: 205px; top: 22px; font-family: "Noto Sans TC", sans-serif; font-weight: 400; font-size: 28px; color: #ffffff; letter-spacing: 1px; }
  .brand-slogan { position: absolute; left: 205px; top: 66px; font-family: "Noto Sans TC", sans-serif; font-weight: 400; font-size: 40px; color: #ffffff; letter-spacing: 1px; }

  .nav-ribbon { position: absolute; left: 537px; top: 203px; width: 560px; height: 80px; }
  .main-nav { position: absolute; left: 537px; top: 225px; width: 540px; height: 20px; }
  .main-nav a { position: absolute; top: 0; font-weight: 700; font-size: 14px; color: var(--nav-text); text-decoration: none; }

  .intro-title { position: absolute; left: 69px; top: 332px; font-weight: 300; font-size: 29px; color: var(--heading-grey); }
  .intro-text { position: absolute; left: 69px; top: 372px; width: 960px; font-size: 13px; line-height: 17.5px; color: var(--body-text); }

  .column { position: absolute; top: 456px; width: 320px; }
  .column-left { left: 69px; }
  .column-right { left: 449px; }
  .column h3 { font-weight: 400; font-size: 13px; color: var(--accent-orange); margin-bottom: 6px; }
  .column p { font-size: 13px; line-height: 17.2px; color: var(--body-text); }

  .like-box { position: absolute; left: 904px; top: 458px; width: 119px; height: 29px;
    background: linear-gradient(180deg, #fafafa, #e2e2e2); font-size: 9px; line-height: 11px; color: #6a6a6a; padding: 3px 6px; }
  .like-button { position: absolute; right: 10px; top: 10px; width: 32px; height: 13px; border: 1px solid #b8c2d6; background: #eef1f7; font-size: 8px; line-height: 11px; text-align: center; color: #3b4f7a; }

  .notes-deco { position: absolute; left: 883px; top: 528px; width: 181px; height: 102px;
    background: radial-gradient(ellipse at 40% 50%, #d6d6d6 0%, #ececec 45%, rgba(255,255,255,0) 75%); }

  .site-footer { position: absolute; left: 0; top: 640px; width: 1091px; height: 42px; background: var(--band-dark); }
  .site-footer p { position: absolute; left: 69px; top: 14px; font-size: 11px; letter-spacing: 0.5px; color: var(--footer-text); }
</style>
</head>
<body>
  <div class="site">
    <div class="top-band" role="img" aria-label="Sheet music and piano keys banner"></div>
    <div class="header-fade"></div>
    <div class="hero-photo" role="img" aria-label="Violin and bow resting on sheet music"></div>

    <div class="brand-panel">
      <span class="brand-dot"></span>
      <p class="brand-name">悅音藝術</p>
      <p class="brand-slogan">用音樂愉悅您的賓客</p>
    </div>

    <svg class="nav-ribbon" viewBox="0 0 560 80" aria-hidden="true">
      <defs>
        <linearGradient id="ribbonFill" x1="0" y1="0" x2="0" y2="1">
          <stop offset="0" stop-color="#fbfbfb"/>
          <stop offset="1" stop-color="#d4d4d4"/>
        </linearGradient>
      </defs>
      <polygon points="10,0 10,5 0,10 0,62 545,58 540,5 520,0" fill="url(#ribbonFill)"/>
      <polygon points="520,8 556,18 548,74 525,50" fill="#bdbdbd"/>
      <polygon points="525,50 548,74 560,60" fill="#9e9e9e"/>
    </svg>
    <nav class="main-nav">
      <a style="left:27px" href="#">Groups</a>
      <a style="left:124px" href="#">Members</a>
      <a style="left:235px" href="#">Videos</a>
      <a style="left:331px" href="#">Pricing</a>
      <a style="left:428px" href="#">Order</a>
    </nav>

    <h1 class="intro-title">Wedding music</h1>
    <p class="intro-text">Cras neque justo, ultrices at, rhoncus a facilisis eget,nisl. Quisque vitae pede. Nam et augue. Sed a elit. Ut vel massa.&nbsp; Suspendisse nibh pede, ultrices vitae ultrices nec, mollis no nibh In sit amet pede quis leo vulputate&nbsp; hendrerit. Cras laoreet leo et justo auctor condimentum. Quisque vitae pede. Nam et augue. Sed a elit. Ut vel massa.&nbsp;&nbsp; uspendisse nibh pede, ultrices vitae ultrices nec, mollis no nibh. In sit amet pede quis leo vulputate&nbsp; hendrerit. Cras laoreet leo et justo auctor condimentum.</p>

    <section class="column column-left">
      <h3>CRAS NEQUE JUSTO</h3>
      <p>Cras neque justo, ultrices at, rhoncus a facilisis eget,nisl. Quisque vitae pede. Nam et augue. Sed a elit. Ut vel massa. Suspendisse nibh pede, ultrices vitae ultrices nec, mollis no nibh. In sit amet pede quis leo vulputate&nbsp; hendrerit. Cras aoreet leo et justo auctor condimentum. Quisque vitae pede. Nam et augue. Sed a elit. Ut vel massa.</p>
    </section>
    <section class="column column-right">
      <h3>CRAS NEQUE JUSTO</h3>
      <p>Cras neque justo, ultrices at, rhoncus a facilisis eget,nisl. Quisque vitae pede. Nam et augue. Sed a elit. Ut vel massa. Suspendisse nibh pede, ultrices vitae ultrices nec, mollis no nibh. In sit amet pede quis leo vulputate&nbsp; hendrerit. Cras aoreet leo et justo auctor condimentum. Quisque vitae pede. Nam et augue. Sed a elit. Ut vel massa.</p>
    </section>

    <aside class="like-box">Like Us<br>on Chatterpage<span class="like-button">Like</span></aside>
    <div class="notes-deco" role="img" aria-label="Faint treble clef and flowing music staff"></div>

    <footer class="site-footer"><p>Copyright 2011. All rights reserved.</p></footer>
  </div>
</body>
</html>
```